Brightmere Glowworks - Two Pages of Information and Pictures

We need a two page summary of the Service Offerings of Brightmere Glowworks - a company that installs LED Lighting. We've written the copy and picked images and chart that we like and have laid it out a word document.

We're looking for someone to design a more professional page layout than the generic Word Template. Please do not feel the current layout is suggested. It is only laid out this way because Word had that template. Be as creative as you want.

We would like the images and text to be in the same order that it is in now.

We're also in a rush so speed is appreciated. THANK YOU !!

Target Market(s)

Corporate Offices in New York

Industry/Entity Type

Lighting Fixture

Colors
85cae6
87cfc7
9bcb3c
3377b5

Requirements
Must have
• Must include two pages of the copy and images written and provided in the word document that was uploaded. Must use the Brightmere colors in the logo.
Nice to have
• An easy to read flow of images and.

```html
<!DOCTYPE html>
<html lang="en">
<head>
<meta charset="utf-8">
<title>Brightmere Glowworks – Service Overview</title>
<link rel="stylesheet" href="https://fonts.googleapis.com/css2?family=Lato:ital,wght@0,300;0,400;0,700;1,400&family=Oswald:wght@500;700&family=Roboto+Condensed:wght@400;500&display=swap">
<style>
  :root{
    --sky:#85cae6;
    --teal:#87cfc7;
    --lime:#9bcb3c;
    --blue:#3377b5;
    --navy:#1d4f7c;
    --plum:#5b2a5e;
    --ink:#2b2b2b;
    --grey:#e6e6e6;
    --bar-light:#b6dcd6;
    --bar-dark:#5f8f68;
    --band:#333;
    --stage:#eeebe5;
  }
  *{box-sizing:border-box;margin:0;padding:0}
  html,body{width:1200px;height:1200px;overflow:hidden;background:var(--stage)}
  body{position:relative;font-family:"Lato",sans-serif;color:var(--ink)}
  .page{position:absolute;top:190px;width:580px;height:814px;background:#fff;overflow:hidden;box-shadow:0 2px 10px rgba(0,0,0,.18)}
  .page--front{left:12px}
  .page--back{left:608px}
  .page__band{position:absolute;left:0;right:0;bottom:0;height:10px;background:var(--band)}
  .page__art{position:absolute;left:0;top:0;width:580px;height:814px}

  /* front */
  .brand-mark{position:absolute;left:0;right:0;top:566px;text-align:center;font:300 28px "Lato",sans-serif;letter-spacing:2px;color:#5e8a68}
  .offer{position:absolute;left:20px;top:665px;width:540px;height:108px;background:var(--sky);padding:6px 14px;text-align:center}
  .offer__title{font:700 21px/1.1 "Oswald",sans-serif;color:var(--navy);letter-spacing:.3px}
  .offer__text{margin-top:3px;font-size:11.2px;line-height:13.6px;color:#1e2a33}
  .site-url{position:absolute;left:0;right:0;top:780px;text-align:center;font-size:8.5px;letter-spacing:3px;color:#333}

  /* back */
  .title{position:absolute;left:0;right:0;top:20px;text-align:center;font:500 38px "Oswald",sans-serif;color:var(--plum)}
  .section-head{position:absolute;left:20px;font:500 13px "Roboto Condensed",sans-serif;color:#222;display:flex;align-items:center;gap:8px}
  .section-head::before{content:"";width:0;height:0;border-top:6px solid transparent;border-bottom:6px solid transparent;border-left:7px solid var(--blue)}
  .body-copy{position:absolute;left:33px;font-size:8.2px;line-height:10.3px;color:#333}
  .body-copy p+p{margin-top:3px}
  .chart-title{position:absolute;left:0;right:0;top:210px;text-align:center;font-size:11px;color:#333;padding-left:130px}
  .chart{position:absolute;left:133px;top:220px;width:318px;height:176px}
  .savings-table{position:absolute;left:16px;top:423px;width:541px;border-collapse:collapse;font-size:7.4px;table-layout:fixed}
  .savings-table td{border:1px solid #333;height:16px;padding:0 2px;white-space:nowrap;overflow:hidden}
  .savings-table .num{text-align:center}
  .team-photo{position:absolute;left:444px;top:498px;width:113px;height:97px;background:linear-gradient(160deg,#7d5a4c 0%,#4c5c72 55%,#2e3746 100%)}
  .quote{position:absolute;left:16px;width:537px;background:var(--grey);padding:5px 12px 4px 13px;font-style:italic;font-size:10.2px;line-height:13.4px;color:#333}
  .quote__by{font-style:normal;font-size:7.8px}
  .quote::before,.quote::after{position:absolute;font:700 22px Georgia,serif;color:#333;font-style:normal}
  .quote::before{content:"\201C";left:-1px;top:-12px}
  .quote::after{content:"\201D";right:-6px;bottom:-18px}
  .contact{position:absolute;left:0;right:0;top:779px;display:flex;justify-content:center;gap:26px;align-items:center;font-size:9px;color:#333}
  .contact__item{display:flex;align-items:center;gap:8px}
  .contact__phone{font:700 11.5px "Lato",sans-serif}
  .contact svg{width:15px;height:15px}
</style>
</head>
<body>

<section class="page page--front">
  <svg class="page__art" viewBox="0 0 730 1024" preserveAspectRatio="none">
    <defs>
      <linearGradient id="fade" x1="0" y1="0" x2="0" y2="1">
        <stop offset="0" stop-color="#fff"/><stop offset=".35" stop-color="#e8e8e8"/><stop offset="1" stop-color="#fff"/>
      </linearGradient>
      <linearGradient id="kitchen" x1="0" y1="0" x2="1" y2="1"><stop offset="0" stop-color="#d8d6d1"/><stop offset=".6" stop-color="#9d9a94"/><stop offset="1" stop-color="#5a5753"/></linearGradient>
      <linearGradient id="bulbs" x1="0" y1="0" x2="1" y2="1"><stop offset="0" stop-color="#3a2a1d"/><stop offset=".5" stop-color="#9b7447"/><stop offset="1" stop-color="#4a3524"/></linearGradient>
      <linearGradient id="ceiling" x1="0" y1="0" x2="0" y2="1"><stop offset="0" stop-color="#2a2a2a"/><stop offset=".4" stop-color="#b4312d"/><stop offset=".7" stop-color="#e9e3df"/><stop offset="1" stop-color="#2c2c2c"/></linearGradient>
      <linearGradient id="desks" x1="0" y1="0" x2="0" y2="1"><stop offset="0" stop-color="#e4e6e4"/><stop offset=".55" stop-color="#9e968a"/><stop offset="1" stop-color="#5d5348"/></linearGradient>
    </defs>
    <rect role="img" aria-label="Faded photo of a bright open office" x="0" y="500" width="730" height="560" fill="url(#fade)"/>
    <polygon points="0,0 178,0 178,105 0,283" fill="var(--teal)"/>
    <polygon points="115,0 285,0 200,92" fill="var(--sky)"/>
    <polygon points="450,0 620,0 535,92" fill="var(--lime)"/>
    <polygon points="650,85 750,185 650,285 550,185" fill="var(--blue)"/>
    <polygon points="0,320 50,370 0,420" fill="var(--sky)"/>
    <polygon points="118,398 170,450 118,502 66,450" fill="var(--blue)"/>
    <polygon points="690,292 775,377 690,462 605,377" fill="var(--lime)"/>
    <polygon points="593,448 645,500 593,552 541,500" fill="var(--teal)"/>
    <g stroke="#fff" stroke-width="8">
      <polygon role="img" aria-label="Photo of a white office kitchen with LED downlights" points="365,-20 517,132 365,284 213,132" fill="url(#kitchen)"/>
      <polygon role="img" aria-label="Photo of caged filament pendant lights" points="190,102 350,262 190,422 30,262" fill="url(#bulbs)"/>
      <polygon role="img" aria-label="Photo of red ceiling with round suspended LED fixtures" points="540,122 695,277 540,432 385,277" fill="url(#ceiling)"/>
      <polygon role="img" aria-label="Photo of a busy open-plan office with desks" points="372,292 532,452 372,612 212,452" fill="url(#desks)"/>
    </g>
  </svg>

  <div class="brand-mark">BRIGHTMERE</div>

  <div class="offer">
    <h2 class="offer__title">NO UPFRONT COST – TURNKEY LEDS</h2>
    <p class="offer__text">Brightmere Glowworks provides LED lighting as a service – fully implemented and managed LEDs at no upfront cost. Brightmere takes the risk, hassle and capital cost out of adopting LED's energy saving technology. Brightmere guarantees net-savings for customers on day one, and continues to guarantee savings and performance for the full term of the contract. And the savings add up! A project can be installed 2-4 weeks from kickoff, and projects continue to generate savings for up to 10 years.</p>
  </div>
  <div class="site-url">www.brightmereglowworks.com</div>
  <div class="page__band"></div>
</section>

<section class="page page--back">
  <svg class="page__art" viewBox="0 0 730 1024" preserveAspectRatio="none">
    <polygon points="642,0 717,0 680,37" fill="var(--sky)"/>
    <polygon points="92,287 112,307 92,327 72,307" fill="#3aaee0"/>
    <polygon points="32,417 65,450 32,483 -1,450" fill="var(--teal)"/>
    <polygon points="678,319 691,332 678,345 665,332" fill="var(--lime)"/>
    <polygon points="618,470 638,490 618,510 598,490" fill="var(--teal)"/>
    <polygon points="0,972 20,992 0,1012" fill="var(--teal)"/>
    <polygon points="730,972 710,992 730,1012" fill="var(--teal)"/>
  </svg>

  <h1 class="title">Brightmere Glowworks</h1>

  <h3 class="section-head" style="top:69px">Why use Brightmere?</h3>
  <div class="body-copy" style="top:89px;width:524px">
    <p>Brightmere's customers understand the value of LEDs but don't want to deal with the risk, hassle and capital cost on their own. Brightmere starts saving customers money the first month – typically a net-savings of about 4.7 cents a square-foot per month. Brightmere will design aesthetic LED systems and install the best available technology.</p>
    <p>Brightmere provides LEDs at the best cost with its as-a-service structure, which puts the cost of lighting into clients' monthly operating budget for less than they save. By installing projects immediately, Brightmere eliminates the cost of foregone savings that would accumulate from delayed implementation.</p>
    <p>It can be risky to adopt new technology, especially when salespeople try to sell more than is needed. Brightmere has access to better equipment and at better cost than is widely available on the open market and passes that quality and savings on to its customers. Brightmere guarantees performance for 5 years, which removes the risk of a failed project.</p>
  </div>

  <div class="chart-title" style="padding-left:0">Annual and Total Net-Savings of 250,000 ft2 Customer</div>
  <svg class="chart" viewBox="0 5 400 235" font-family="Lato, sans-serif" font-size="6.5" fill="#333">
    <g stroke="#999" stroke-width=".6">
      <line x1="45" y1="28" x2="360" y2="28"/><line x1="45" y1="58.5" x2="360" y2="58.5"/>
      <line x1="45" y1="89" x2="360" y2="89"/><line x1="45" y1="119.5" x2="360" y2="119.5"/>
      <line x1="45" y1="150" x2="360" y2="150"/><line x1="45" y1="180.5" x2="360" y2="180.5"/>
      <line x1="45" y1="211" x2="360" y2="211"/>
    </g>
    <g text-anchor="end">
      <text x="38" y="30">$300</text><text x="38" y="60.5">$250</text><text x="38" y="91">$200</text>
      <text x="38" y="121.5">$150</text><text x="38" y="152">$100</text><text x="38" y="182.5">$50</text><text x="38" y="213">$-</text>
    </g>
    <g>
      <text x="366" y="30">$2.0</text><text x="366" y="48">$1.8</text><text x="366" y="67">$1.6</text>
      <text x="366" y="85">$1.4</text><text x="366" y="103">$1.2</text><text x="366" y="122">$1.0</text>
      <text x="366" y="140">$0.8</text><text x="366" y="158">$0.6</text><text x="366" y="177">$0.4</text>
      <text x="366" y="195">$0.2</text><text x="366" y="213">$0.0</text>
    </g>
    <text transform="translate(10,120) rotate(-90)" text-anchor="middle" font-size="6">Thousands</text>
    <text transform="translate(392,120) rotate(-90)" text-anchor="middle" font-size="6">Millions</text>
    <g fill="var(--bar-light)">
      <rect x="49" y="150" width="10" height="61"/><rect x="81" y="150" width="10" height="61"/>
      <rect x="112" y="150" width="10" height="61"/><rect x="144" y="150" width="10" height="61"/>
      <rect x="175" y="150" width="10" height="61"/>
    </g>
    <g fill="var(--bar-dark)">
      <rect x="60" y="125.6" width="10" height="85.4"/><rect x="92" y="125.6" width="10" height="85.4"/>
      <rect x="123" y="125.6" width="10" height="85.4"/><rect x="155" y="125.6" width="10" height="85.4"/>
      <rect x="186" y="125.6" width="10" height="85.4"/><rect x="218" y="64.6" width="10" height="146.4"/>
      <rect x="250" y="64.6" width="10" height="146.4"/><rect x="281" y="64.6" width="10" height="146.4"/>
      <rect x="313" y="64.6" width="10" height="146.4"/><rect x="345" y="64.6" width="10" height="146.4"/>
    </g>
    <polyline fill="none" stroke="#aaa" stroke-width="1.2" points="60,198 92,185 123,173 155,160 186,147 218,125 250,103 281,81 313,59 345,37"/>
    <g text-anchor="middle">
      <text x="60" y="223">1</text><text x="92" y="223">2</text><text x="123" y="223">3</text><text x="155" y="223">4</text><text x="186" y="223">5</text>
      <text x="218" y="223">6</text><text x="250" y="223">7</text><text x="281" y="223">8</text><text x="313" y="223">9</text><text x="345" y="223">10</text>
    </g>
    <g font-size="5.5">
      <rect x="62" y="230" width="16" height="3.5" fill="var(--bar-light)"/><text x="84" y="234">Annual Brightmere Service</text>
      <rect x="178" y="230" width="16" height="3.5" fill="var(--bar-dark)"/><text x="197" y="234">Annual Net-Savings</text>
      <line x1="266" y1="232" x2="282" y2="232" stroke="#aaa" stroke-width="1.2"/><text x="286" y="234">Total Net-Savings</text>
    </g>
  </svg>

  <table class="savings-table">
    <colgroup><col style="width:48px"><col style="width:107px"><col span="10"></colgroup>
    <tr><td>250000 ft2</td><td>Year</td><td class="num">1</td><td class="num">2</td><td class="num">3</td><td class="num">4</td><td class="num">5</td><td class="num">6</td><td class="num">7</td><td class="num">8</td><td class="num">9</td><td class="num">10</td></tr>
    <tr><td>0.04 $/ft2</td><td>Annual Brightmere Service</td><td>$100,000</td><td>$100,000</td><td>$100,000</td><td>$100,000</td><td>$100,000</td><td></td><td></td><td></td><td></td><td></td></tr>
    <tr><td>0.08 $/ft2</td><td>Annual Net-Savings</td><td>$140,000</td><td>$140,000</td><td>$140,000</td><td>$140,000</td><td>$140,000</td><td>$240,000</td><td>$240,000</td><td>$240,000</td><td>$240,000</td><td>$240,000</td></tr>
    <tr><td></td><td>Total Net-Savings</td><td>$140,000</td><td>$280,000</td><td>$420,000</td><td>$560,000</td><td>$700,000</td><td>$940,000</td><td>$1,180,000</td><td>$1,420,000</td><td>$1,660,000</td><td>$1,900,000</td></tr>
  </table>

  <h3 class="section-head" style="top:505px">The Best Team in LEDs</h3>
  <div class="body-copy" style="top:524px;width:398px">
    <p>Brightmere is a team of lighting experts who get the evolution of lighting and efficiency. Simply put, we come in up every day with one goal: to provide an excellent service that saves money and uses less electricity. Part of the team focuses on the supply chain of the very best equipment that customers have come to appreciate. Part of the team focuses on the project management of each installation. And, part of the team focuses on resolving any questions customers might have in their transition. Together we make up the best team in LEDs and work tirelessly to make it easy to upgrade.</p>
  </div>
  <div class="team-photo" role="img" aria-label="Photo of the installation team in matching shirts, seen from behind"></div>

  <h3 class="section-head" style="top:591px">Testimonials</h3>
  <blockquote class="quote" style="top:620px">Brightmere made a huge improvement in the lighting for our headquarters. The installation process was as smooth as can be and the service since has been excellent. <span class="quote__by">– Ferncroft Health</span></blockquote>
  <blockquote class="quote" style="top:668px">In a museum, quality lighting is paramount. Brightmere has been a great partner in helping us transition to LEDs that look great, save us money, and make lighting management so much simpler. <span class="quote__by">– Harborview Museum of Art, New York</span></blockquote>
  <blockquote class="quote" style="top:716px">We are so happy to have had Brightmere's help building out our new office space – they put their lighting expertise to work delivering beautiful LEDs and fixtures. It was cost-effective, removed lighting from the build-out budget, and it's been a joy to work with them since</blockquote>

  <div class="contact">
    <span class="contact__item">
      <svg viewBox="0 0 16 16" aria-hidden="true"><path d="M2 6c0-2 2-3 6-3s6 1 6 3l-2 1-1-2H5L4 7z M4 8h8l1 5H3z" fill="#777"/><circle cx="8" cy="10.5" r="1.4" fill="#fff"/></svg>
      <span class="contact__phone">555 010 GLOW</span>
    </span>
    <span class="contact__item">
      <svg viewBox="0 0 16 16" aria-hidden="true"><rect x="1" y="3" width="14" height="10" fill="#777"/><path d="M1.5 3.5 8 9l6.5-5.5" fill="none" stroke="#fff" stroke-width="1.2"/></svg>
      <span>customers@brightmereglowworks.com</span>
    </span>
    <span class="contact__item">
      <svg viewBox="0 0 16 16" aria-hidden="true" fill="none" stroke="#777" stroke-width="1.2"><circle cx="8" cy="8" r="6.5"/><ellipse cx="8" cy="8" rx="3" ry="6.5"/><line x1="1.5" y1="8" x2="14.5" y2="8"/><line x1="2.5" y1="4.5" x2="13.5" y2="4.5"/><line x1="2.5" y1="11.5" x2="13.5" y2="11.5"/></svg>
      <span>www.brightmereglowworks.com</span>
    </span>
  </div>
  <div class="page__band"></div>
</section>

</body>
</html>
```